Stationary For Harbor Allies
Harbor Allies
Project: Stationary For Harbor Allies
Stationary For Harbor Allies - Consulting
Creative Brief
Professional
Lou Brannick
President
547 Marlow Ln Millbrook, OK 74032
lbrannick@harborallies4.com
www.harborallies4.com
I will need letterhead and envelopes as well as business cards. Feel free to try different fonts.
quelnor42 quelnor42
Designers, Please focus more on the letterhead and envelopes than the business cards. Thanks!

```html
<!DOCTYPE html>
<html lang="en">
<head>
<meta charset="utf-8">
<title>Harbor Allies – Business Card</title>
<link href="https://fonts.googleapis.com/css2?family=Open+Sans:wght@400;600;700&display=swap" rel="stylesheet">
<style>
  :root {
    --bg: #e9e9ec;
    --brand-blue: #1f5fb0;
    --brand-deep: #0f3f86;
    --brand-light: #2f78cc;
    --ink: #3a4250;
    --ink-soft: #6b7380;
    --swoosh: #c9ccd2;
    --paper: #ffffff;
  }
  * { margin: 0; padding: 0; box-sizing: border-box; }
  html, body { width: 1200px; height: 904px; overflow: hidden; }
  body {
    background: var(--bg);
    font-family: "Open Sans", Arial, sans-serif;
    position: relative;
  }
  .card {
    position: absolute;
    width: 700px;
    height: 400px;
    overflow: hidden;
    box-shadow: 0 6px 18px rgba(0,0,0,0.18);
  }
  .card--back {
    left: 120px; top: 40px;
    background: radial-gradient(ellipse at 50% 45%, var(--brand-light) 0%, var(--brand-blue) 45%, var(--brand-deep) 100%);
    display: flex; align-items: center; justify-content: center;
  }
  .back-mark {
    display: flex; align-items: center; gap: 16px;
    color: #ffffff;
    font-size: 44px; font-weight: 600; letter-spacing: 1px;
  }
  .back-mark .dot {
    width: 26px; height: 26px; border-radius: 50%; background: #ffffff;
  }
  .card--front { left: 380px; top: 464px; background: var(--paper); }
  .front-wave { position: absolute; inset: 0; }
  .brand {
    position: absolute; left: 60px; top: 180px;
    display: flex; align-items: center; gap: 14px;
    color: var(--brand-blue);
    font-size: 30px; font-weight: 600;
  }
  .brand .dot { width: 22px; height: 22px; border-radius: 50%; background: var(--brand-blue); }
  .contact { position: absolute; left: 392px; top: 48px; color: var(--ink); font-size: 13px; line-height: 1.45; }
  .contact .name { color: var(--brand-blue); font-weight: 700; font-size: 16px; }
  .contact .title { color: var(--ink-soft); margin-bottom: 12px; }
  .contact .address { margin-bottom: 12px; }
  .contact-line { display: flex; align-items: center; gap: 8px; }
  .contact-line svg { width: 12px; height: 12px; flex: none; }
  .website {
    position: absolute; right: 30px; bottom: 28px;
    color: #ffffff; font-size: 14px; letter-spacing: 0.3px;
  }
</style>
</head>
<body>

<section class="card card--back" aria-label="Business card back">
  <div class="back-mark"><span class="dot"></span>Harbor Allies</div>
</section>

<section class="card card--front" aria-label="Business card front">
  <svg class="front-wave" viewBox="0 0 700 400" preserveAspectRatio="none" aria-hidden="true">
    <defs>
      <linearGradient id="waveFill" x1="0" y1="0" x2="1" y2="1">
        <stop offset="0" stop-color="#2a6fc2"/>
        <stop offset="1" stop-color="#123f86"/>
      </linearGradient>
    </defs>
    <path d="M0 330 C 200 345, 420 300, 700 205 L700 400 L0 400 Z" fill="var(--swoosh)"/>
    <path d="M0 345 C 210 358, 430 318, 700 222 L700 400 L0 400 Z" fill="url(#waveFill)"/>
  </svg>

  <div class="brand"><span class="dot"></span>Harbor Allies</div>

  <div class="contact">
    <div class="name">Lou Brannick</div>
    <div class="title">President</div>
    <div class="address">547 Marlow Ln<br>Millbrook, OK 74032</div>
    <div class="contact-line">
      <svg viewBox="0 0 12 12"><rect x="3" y="0.5" width="6" height="11" rx="1.2" fill="var(--brand-blue)"/></svg>
      (817) 555-0142
    </div>
    <div class="contact-line">
      <svg viewBox="0 0 12 12"><path d="M2 1h3l1 3-1.5 1a7 7 0 0 0 2.5 2.5L8 6l3 1v3a1 1 0 0 1-1 1A9 9 0 0 1 1 2a1 1 0 0 1 1-1z" fill="var(--brand-blue)"/></svg>
      (817) 555-0187
    </div>
    <div class="contact-line">
      <svg viewBox="0 0 12 12"><rect x="1" y="4" width="10" height="6" fill="var(--brand-blue)"/><rect x="3" y="1" width="6" height="3" fill="var(--brand-blue)"/></svg>
      (210) 555-0163
    </div>
    <div class="contact-line">
      <svg viewBox="0 0 12 12"><rect x="0.5" y="2.5" width="11" height="7" fill="var(--brand-blue)"/><path d="M0.5 2.5 6 7l5.5-4.5" fill="none" stroke="#fff" stroke-width="1"/></svg>
      lbrannick@harborallies4.com
    </div>
  </div>

  <div class="website">www.harborallies4.com</div>
</section>

</body>
</html>
```